Real Estate Agent needs business card design

We have logo designed already, want to have business card designed. Very interested in those smaller size business card as they look very trendy. Business name is called TOVANE REALTY

Industry/Entity Type

Business

```html
<!DOCTYPE html>
<html lang="en">
<head>
<meta charset="utf-8">
<title>Tovane Realty – Business Card</title>
<link rel="stylesheet" href="https://fonts.googleapis.com/css2?family=Cinzel:wght@400;500&family=Arimo:wght@400;700&display=swap">
<style>
  :root {
    --stage: #232323;
    --card-white: #ffffff;
    --card-shade: #e4e4e4;
    --gold: #c9a46c;
    --gold-text: #b8925a;
    --ink: #1e1e1e;
    --icon-grey: #6d6d6d;
  }
  * { margin: 0; padding: 0; box-sizing: border-box; }
  html, body {
    width: 1200px; height: 997px; overflow: hidden;
    background: var(--stage);
  }
  .stage { position: relative; width: 1200px; height: 997px; }

  .card {
    position: absolute; top: 318px; height: 329px;
    overflow: hidden;
  }
  .card--front {
    left: 50px; width: 548px;
    background: linear-gradient(90deg, var(--card-shade) 0%, var(--card-white) 45%, var(--card-white) 100%);
  }
  .card--back {
    left: 611px; width: 549px;
    background: linear-gradient(90deg, var(--card-white) 0%, var(--card-white) 60%, #eeeeee 100%);
  }

  .seal {
    position: absolute; width: 392px; height: 392px; border-radius: 50%;
    background: var(--gold); top: -14px;
  }
  .card--front .seal { left: 360px; }
  .card--back .seal { left: -201px; }

  .brand {
    position: absolute; font-family: "Cinzel", serif; font-weight: 500;
    white-space: nowrap; line-height: 1;
  }
  .brand--front { left: 29px; top: 115px; font-size: 27px; color: var(--ink); }
  .brand--seal-left { right: 0; top: 196px; font-size: 32px; color: var(--card-white); }
  .brand--seal-right { left: 9px; top: 199px; font-size: 32px; color: var(--card-white); }
  .brand--back { left: 0; width: 740px; text-align: center; top: 189px; font-size: 30px; color: var(--ink); transform: translateX(-1px); }
  .card--back .brand--back { left: 0; width: 740px; }

  .contact {
    position: absolute; left: 29px; top: 182px;
    font-family: "Arimo", Arial, sans-serif; font-size: 13px; line-height: 1.25;
  }
  .contact__name { color: var(--gold-text); font-weight: 700; font-size: 14.5px; letter-spacing: 0.3px; }
  .contact__role { color: var(--ink); font-weight: 700; margin-bottom: 13px; }
  .contact__address { color: var(--gold-text); margin-bottom: 17px; }
  .contact__line { display: flex; align-items: center; gap: 8px; color: var(--ink); height: 21px; }
  .contact__icon { width: 14px; height: 14px; flex: none; }
</style>
</head>
<body>
<main class="stage">
  <section class="card card--front">
    <div class="seal"></div>
    <p class="brand brand--front">Tovane Realty</p>
    <p class="brand brand--seal-left">Tovane</p>
    <div class="contact">
      <p class="contact__name">DANIEL HART</p>
      <p class="contact__role">Director</p>
      <p class="contact__address">PO Box 512 Kelmore<br>B.C. QLD 4870</p>
      <p class="contact__line">
        <svg class="contact__icon" viewBox="0 0 14 14" aria-hidden="true">
          <circle cx="7" cy="7" r="7" fill="var(--icon-grey)"/>
          <path d="M3.5 6.2 Q7 3.6 10.5 6.2 L9.6 7.2 L8.3 6.6 L8.3 5.8 Q7 5.4 5.7 5.8 L5.7 6.6 L4.4 7.2 Z M5 8 H9 L9.6 10 H4.4 Z" fill="#fff"/>
        </svg>
        0455218730
      </p>
      <p class="contact__line">
        <svg class="contact__icon" viewBox="0 0 14 14" aria-hidden="true">
          <circle cx="7" cy="7" r="7" fill="var(--icon-grey)"/>
          <rect x="3.5" y="4.5" width="7" height="5" fill="none" stroke="#fff" stroke-width="1"/>
          <path d="M3.5 4.5 L7 7.3 L10.5 4.5" fill="none" stroke="#fff" stroke-width="1"/>
        </svg>
        daniel@harlowmail.biz
      </p>
    </div>
  </section>

  <section class="card card--back">
    <div class="seal"></div>
    <p class="brand brand--seal-right">Realty</p>
    <p class="brand brand--back">Tovane Realty</p>
  </section>
</main>
</body>
</html>
```